Its time for your mortgage check up

Complete Ad for Social Media Campaign

Target Market(s)

potential mortgage customers

Colors

Designer to choose colors to be used in the design.

Requirements
Must have
• Rates are dropping
• Its Time for your Mortgage Check Up
• Free Written Proposal Detailing Potential Benefits and Savings
• * Same Day Response
• * No Credit Check
• * No Fee or Obligation
• Contact us today at (800) 555-0147
• Blue Harbor Lending Services, Inc.
• 7200 Marlowe Lane, Ellicott City, MD 21043
• NMLS #318760

```html
<!DOCTYPE html>
<html lang="en">
<head>
<meta charset="utf-8">
<title>Rates Are Dropping – Mortgage Check Up</title>
<link rel="stylesheet" href="https://fonts.googleapis.com/css2?family=Montserrat:wght@300;400;500;600;700;800&display=swap">
<style>
  :root {
    --gold: #ab9c3f;
    --navy: #0d3556;
    --navy-veil: rgba(9, 46, 80, 0.9);
    --brand-blue: #0b5aa2;
    --white: #ffffff;
    --ink: #2a2a2a;
    --photo-light: #c9cbbd;
    --photo-mid: #a4a897;
    --photo-warm: #c89a7c;
  }
  html, body {
    margin: 0;
    padding: 0;
    width: 1170px;
    height: 1200px;
    overflow: hidden;
    background: #ffffff;
  }
  .canvas {
    position: relative;
    width: 1170px;
    height: 1200px;
    overflow: hidden;
  }
  .ad {
    position: absolute;
    left: 0;
    top: 0;
    width: 1241px;
    height: 1241px;
    transform: scale(0.9428, 0.967);
    transform-origin: 0 0;
    font-family: "Montserrat", Arial, sans-serif;
    overflow: hidden;
    background: var(--white);
  }
  .top-band {
    position: absolute;
    left: 0; top: 0;
    width: 1241px; height: 303px;
    background: var(--gold);
    overflow: hidden;
  }
  .brand-disc {
    position: absolute;
    left: 56px; top: -1px;
    width: 446px; height: 446px;
    border-radius: 50%;
    background: var(--white);
  }
  .brand-name {
    position: absolute;
    left: 90px; top: 150px;
    width: 380px;
    text-align: center;
    font-weight: 700;
    font-size: 34px;
    line-height: 1.15;
    color: var(--brand-blue);
  }
  .headline {
    position: absolute;
    left: 563px;
    margin: 0;
    color: var(--white);
    font-size: 106px;
    line-height: 1;
    letter-spacing: 1px;
    white-space: nowrap;
  }
  .headline--light { top: 57px; font-weight: 500; }
  .headline--bold { top: 157px; font-weight: 800; }

  .hero-photo {
    position: absolute;
    left: 0; top: 303px;
    width: 1241px; height: 698px;
    background:
      radial-gradient(ellipse 260px 300px at 600px 240px, var(--photo-warm) 0%, rgba(200,154,124,0) 100%),
      radial-gradient(ellipse at 50% 40%, var(--photo-light) 0%, var(--photo-mid) 100%);
  }
  .offer-band {
    position: absolute;
    left: 0; top: 688px;
    width: 1241px; height: 313px;
    background: var(--navy-veil);
  }
  .offer-kicker {
    position: absolute;
    left: 106px; top: 720px;
    margin: 0;
    font-size: 58px;
    font-weight: 500;
    line-height: 1;
    color: var(--white);
    white-space: nowrap;
  }
  .offer-title {
    position: absolute;
    left: 104px; top: 778px;
    margin: 0;
    font-size: 91px;
    font-weight: 800;
    line-height: 1;
    color: var(--white);
    white-space: nowrap;
  }
  .offer-sub {
    position: absolute;
    left: 107px; top: 873px;
    margin: 0;
    font-size: 25px;
    font-weight: 600;
    line-height: 1;
    color: var(--white);
    white-space: nowrap;
  }
  .benefits {
    position: absolute;
    left: 83px; top: 918px;
    width: 1075px; height: 64px;
    box-sizing: border-box;
    border: 2px solid #d9d3a8;
    border-radius: 4px;
    background: var(--white);
    display: flex;
    align-items: center;
    justify-content: space-around;
    padding: 0 20px;
    margin: 0;
    list-style: none;
  }
  .benefit {
    display: flex;
    align-items: center;
    gap: 6px;
    font-size: 28px;
    font-weight: 600;
    color: var(--ink);
    white-space: nowrap;
  }
  .benefit svg { width: 26px; height: 26px; }

  .contact-bar {
    position: absolute;
    left: 0; top: 1001px;
    width: 1241px; height: 85px;
  }
  .contact-bar svg.bar-bg { position: absolute; left: 0; top: 0; }
  .contact-cta {
    position: absolute;
    left: 82px; top: 0;
    height: 85px;
    display: flex; align-items: center;
    font-size: 52px;
    font-weight: 800;
    color: var(--white);
    white-space: nowrap;
  }
  .contact-phone {
    position: absolute;
    left: 695px; top: 0;
    height: 85px;
    display: flex; align-items: center; gap: 12px;
    font-size: 54px;
    font-weight: 700;
    color: var(--white);
    white-space: nowrap;
  }
  .contact-phone svg { width: 54px; height: 54px; }

  .footer-company {
    position: absolute;
    left: 82px; top: 1106px;
    margin: 0;
    font-size: 27px;
    font-weight: 600;
    line-height: 1;
    color: var(--brand-blue);
  }
  .footer-line {
    position: absolute;
    left: 81px;
    margin: 0;
    font-size: 27px;
    font-weight: 400;
    line-height: 1;
    color: var(--ink);
    white-space: nowrap;
  }
  .footer-line--address { top: 1147px; }
  .footer-line--license { top: 1179px; }
  .housing-badge {
    position: absolute;
    left: 1062px; top: 1112px;
    width: 98px; height: 106px;
  }
</style>
</head>
<body>
<div class="canvas">
  <div class="ad">
    <header class="top-band">
      <div class="brand-disc"></div>
      <div class="brand-name">Blue Harbor Lending Services, Inc.</div>
      <h1 class="headline headline--light">RATES ARE</h1>
      <h1 class="headline headline--bold">DROPPING</h1>
    </header>

    <div class="hero-photo" role="img" aria-label="Photo of an excited woman cheering with raised fists as banknotes fall around her"></div>

    <section class="offer-band"></section>
    <p class="offer-kicker">ITS TIME FOR YOUR</p>
    <h2 class="offer-title">MORTGAGE CHECK UP</h2>
    <p class="offer-sub">Free Written Proposal Detailing Potential Benefits and Savings</p>

    <ul class="benefits">
      <li class="benefit"><svg viewBox="0 0 26 26"><path d="M3 14 L10 22 L24 3" fill="none" stroke="#0b5aa2" stroke-width="3.2" stroke-linecap="round" stroke-linejoin="round"/></svg>Same Day Response</li>
      <li class="benefit"><svg viewBox="0 0 26 26"><path d="M3 14 L10 22 L24 3" fill="none" stroke="#0b5aa2" stroke-width="3.2" stroke-linecap="round" stroke-linejoin="round"/></svg>No Credit Check</li>
      <li class="benefit"><svg viewBox="0 0 26 26"><path d="M3 14 L10 22 L24 3" fill="none" stroke="#0b5aa2" stroke-width="3.2" stroke-linecap="round" stroke-linejoin="round"/></svg>No Fee or Obligation</li>
    </ul>

    <div class="contact-bar">
      <svg class="bar-bg" width="1241" height="85" viewBox="0 0 1241 85">
        <rect width="1241" height="85" fill="#ab9c3f"/>
        <polygon points="681,0 1241,0 1241,85 650,85" fill="#0b5aa2"/>
      </svg>
      <div class="contact-cta">CONTACT US TODAY</div>
      <div class="contact-phone">
        <svg viewBox="0 0 54 54">
          <circle cx="27" cy="27" r="24" fill="none" stroke="#ffffff" stroke-width="3.5"/>
          <path d="M19 14 C16 16 15 20 17 25 C19 31 24 37 30 40 C34 42 38 41 40 38 L36 33 C35 32 33 32 32 33 L30 35 C27 33 23 29 21 25 L23 23 C24 22 24 20 23 19 Z" fill="#ffffff"/>
        </svg>
        (800) 555-0147
      </div>
    </div>

    <p class="footer-company">Blue Harbor Lending Services, Inc.</p>
    <p class="footer-line footer-line--address">7200 Marlowe Lane, Ellicott City, MD 21043</p>
    <p class="footer-line footer-line--license">NMLS #318760</p>

    <svg class="housing-badge" viewBox="0 0 98 106" aria-hidden="true">
      <rect x="4" y="8" width="90" height="90" rx="4" fill="#111111"/>
    </svg>
  </div>
</div>
</body>
</html>
```